Personal letterhead and stationary

I am looking for someone to design letterhead and stationary set for my personal use. I want something simple and timeless with a little bit of color. I like photography, computers and writing.

```html
<!DOCTYPE html>
<html lang="en">
<head>
<meta charset="utf-8">
<title>Jonathan Roy Hayes — Letterhead</title>
<link rel="stylesheet" href="https://fonts.googleapis.com/css2?family=Bebas+Neue&family=Oswald:wght@400&display=swap">
<style>
  :root {
    --canvas: #ffffff;
    --sheet: #f6f6f6;
    --header-band: #efefef;
    --name-primary: #8e8e8e;
    --name-secondary: #cdcdcd;
    --contact: #6e6e6e;
  }
  html, body {
    margin: 0;
    padding: 0;
    width: 1200px;
    height: 1000px;
    overflow: hidden;
    background: var(--canvas);
  }
  .letterhead {
    position: absolute;
    left: 320px;
    top: 100px;
    width: 560px;
    height: 800px;
    background: var(--sheet);
    overflow: hidden;
  }
  .letterhead__header {
    position: absolute;
    left: 0;
    top: 0;
    width: 100%;
    height: 100px;
    background: linear-gradient(to bottom, var(--header-band), var(--sheet));
  }
  .letterhead__name {
    position: absolute;
    left: 13px;
    top: 11px;
    margin: 0;
    font-family: "Bebas Neue", "Oswald", sans-serif;
    font-weight: 400;
    font-size: 86px;
    line-height: 1;
    letter-spacing: -1.2px;
    white-space: nowrap;
  }
  .letterhead__name-first { color: var(--name-primary); }
  .letterhead__name-rest { color: var(--name-secondary); margin-left: 10px; }
  .letterhead__contact {
    position: absolute;
    left: 16px;
    top: 86px;
    margin: 0;
    font-family: "Oswald", sans-serif;
    font-size: 7px;
    line-height: 1;
    color: var(--contact);
    letter-spacing: -0.05px;
    white-space: nowrap;
  }
</style>
</head>
<body>
  <main class="letterhead">
    <header class="letterhead__header">
      <h1 class="letterhead__name">
        <span class="letterhead__name-first">JONATHAN</span><span class="letterhead__name-rest">ROY HAYES</span>
      </h1>
      <p class="letterhead__contact">4127 ELM ST S, DENVER, CO 80209, UNITED STATES | PHONE: +1 303-555-0148 | HELLO@JRHAYES.COM</p>
    </header>
  </main>
</body>
</html>
```